Corporate Brochure Cover Design

We need a design for a corporate A4 Size portfolio cover (front and back) which we will be distributing. to our commercial clients.

We are a professional plumbing company that is an industry leader for service we provide to our clients and technology we use. The design needs to incorporate the colours black, red, white and silver and needs to include our logo. We dont have any slogans or mottos... If you wanted to use something it could be "Delivering exceptional service...Always!" however i dont want it to b the focal point of the cover.

Im looking for something professional and modern that has the WOW factor!

Size is A4 - both front and back covers. You can include pictures as well or sample pictures of where we can source and put our own team pictures.

if you have any questions, please do not hesitate to contact me.

Target Market(s)

Our commercial & strata clients - professional industry.

Industry/Entity Type

Commercial

Font styles to use
Sans Serif

Requirements
Must have
• Red, black, white, silver as the colour scheme.
• Include the logo.
Nice to have
• Modern design and something that makes the client go WOW before they open the brochure.
Should not have
• lots of text

```html
<!DOCTYPE html>
<html lang="en">
<head>
<meta charset="utf-8">
<title>Northline Brochure Covers</title>
<link rel="stylesheet" href="https://fonts.googleapis.com/css2?family=Michroma&family=Open+Sans:wght@400&display=swap">
<style>
  :root {
    --stage: #a6a6a6;
    --cover: #231f20;
    --red: #c41e2e;
    --white: #ffffff;
    --silver: #d9dde2;
    --faint: #3b3536;
    --contact: #e8e8e8;
  }
  html, body {
    margin: 0;
    width: 1200px;
    height: 1200px;
    overflow: hidden;
    background: var(--stage);
  }
  .canvas { position: relative; width: 1200px; height: 1200px; }
  .cover { position: absolute; width: 478px; height: 676px; display: block; }
  .cover--front { left: 90px; top: 226px; }
  .cover--back { left: 639px; top: 224px; }
  .brand-name { font-family: "Michroma", sans-serif; fill: var(--white); }
  .headline { font-family: "Michroma", sans-serif; fill: var(--white); letter-spacing: 5px; }
  .intro { font-family: "Open Sans", sans-serif; fill: var(--red); font-size: 15px; }
  .contact { font-family: "Open Sans", sans-serif; fill: var(--contact); font-size: 7.5px; }
</style>
</head>
<body>
<div class="canvas">

  <!-- Front cover -->
  <svg class="cover cover--front" viewBox="0 0 598 845" xmlns="http://www.w3.org/2000/svg">
    <defs>
      <linearGradient id="photoTone" x1="0" y1="0" x2="1" y2="1">
        <stop offset="0" stop-color="#f2f4f3"/>
        <stop offset="0.6" stop-color="#d8dbdd"/>
        <stop offset="1" stop-color="#9fa3a8"/>
      </linearGradient>
    </defs>
    <rect class="cover-bg" width="598" height="845" fill="var(--cover)"/>

    <g class="brand">
      <circle cx="178" cy="108" r="7" fill="var(--red)"/>
      <text class="brand-name" x="196" y="120" font-size="34">NORTHLINE</text>
    </g>

    <g class="photo-band">
      <path role="img" aria-label="Photo: relaxed businessman at his office desk"
            d="M0 193 Q170 186 345 268 Q170 330 0 452 Z" fill="url(#photoTone)"/>
      <path class="red-sweep" d="M345 268 Q470 228 598 220 L598 248 Q520 285 470 335 Z" fill="var(--red)"/>
      <path role="img" aria-label="Photo: busy receptionist handling several phones"
            d="M130 390 Q300 300 470 335 L318 506 Z" fill="url(#photoTone)"/>
      <path role="img" aria-label="Photo: worker carrying a tall stack of files"
            d="M470 335 Q530 280 598 248 L598 435 Q530 400 470 335 Z" fill="url(#photoTone)"/>
    </g>

    <text class="headline" text-anchor="middle" x="276" y="668" font-size="25">YOUR MAIN</text>
    <text class="headline" text-anchor="middle" x="276" y="708" font-size="25">HEADLINE HERE</text>

    <text class="intro" x="60" y="751">Lorem Ipsum is simply dummy text of the printing and typesetting</text>
    <text class="intro" x="60" y="768">industry. Lorem Ipsum has been the industry's standard dummy</text>
  </svg>

  <!-- Back cover -->
  <svg class="cover cover--back" viewBox="0 0 597 845" xmlns="http://www.w3.org/2000/svg">
    <rect class="cover-bg" width="597" height="845" fill="var(--cover)"/>

    <text class="brand-name" text-anchor="middle" x="298" y="440" font-size="62" fill="var(--faint)" style="fill: var(--faint)">NORTHLINE</text>

    <g class="footer-brand">
      <circle cx="57" cy="781" r="4" fill="var(--red)"/>
      <text class="brand-name" x="66" y="786" font-size="14">NORTHLINE</text>
    </g>

    <g class="contact-list">
      <circle cx="198" cy="776" r="5" fill="var(--red)"/>
      <path d="M195 776 q3 -3 6 0" stroke="var(--white)" stroke-width="1.2" fill="none"/>
      <text class="contact" x="208" y="779">+000 493 6689</text>
      <circle cx="198" cy="790" r="5" fill="var(--red)"/>
      <path d="M195 790 q3 -3 6 0" stroke="var(--white)" stroke-width="1.2" fill="none"/>
      <text class="contact" x="208" y="793">+000 270 6414</text>

      <circle cx="276" cy="776" r="5" fill="var(--red)"/>
      <rect x="273" y="774" width="6" height="4" fill="none" stroke="var(--white)" stroke-width="0.9"/>
      <text class="contact" x="286" y="779">Info@emailid.com</text>
      <circle cx="276" cy="790" r="5" fill="var(--red)"/>
      <circle cx="276" cy="790" r="2.6" fill="none" stroke="var(--white)" stroke-width="0.9"/>
      <text class="contact" x="286" y="793">www.website.com</text>

      <line x1="364" y1="770" x2="364" y2="796" stroke="var(--contact)" stroke-width="0.8"/>
      <text class="contact" x="374" y="779">P.O. Box 0000, Kings Road</text>
      <text class="contact" x="374" y="791">Texas 0000, USA</text>
    </g>
  </svg>

</div>
</body>
</html>
```